BrivoPeak Business Card Design Project

We are looking for a modern, clean business card design for our new company. We are a consulting firm focused on the financial services market providing management and IT consulting to banks, insurance companies, etc. Please include our company logo and company contact information from the attached file in the design. Two versions of the logo are attached, either version is acceptable. Logos are available in other file formats if needed. We would like to include the contact information for both our UK and US offices as well as the following information for each individual card holder: Name, position/title, address, phone number and e-mail address.
Updates
Project Deadline Extended
Reason: A last minute trip over seas has prevented us from finalizing the decision. A decision will be made this week. We apologize for the inconvenience.
Industry/Entity Type
Business
Contact Information for Business Card
Company logo.
Company locations and phone numbers for both the US and UK offices.
Company URL.
Cardholder Name
Cardholder Position/title
Cardholder Address
Cardholder Phone Number
Cardholder e-mail Address
Look and feel
Each slider illustrates characteristics of the customer's brand and the style your logo design should communicate.

```html
<!DOCTYPE html>
<html lang="en">
<head>
<meta charset="utf-8">
<title>BrivoPeak Partners – Business Card</title>
<link rel="stylesheet" href="https://fonts.googleapis.com/css2?family=Source+Sans+3:wght@400;600;700&display=swap">
<style>
  :root {
    --navy: #132d54;
    --navy-soft: #1d3a66;
    --ink-grey: #555a60;
    --text-grey: #4a4d52;
    --paper: #ffffff;
    --backdrop: #adadad;
    --font: "Source Sans 3", "Myriad Pro", Arial, sans-serif;
  }
  * { box-sizing: border-box; margin: 0; padding: 0; }
  html, body { width: 1200px; height: 900px; overflow: hidden; }
  body {
    position: relative;
    background: var(--backdrop);
    font-family: var(--font);
  }
  .card {
    position: absolute;
    top: 170px;
    width: 347px;
    height: 561px;
  }
  .card-front { left: 259px; background: var(--paper); color: var(--text-grey); }
  .card-back { left: 631px; background: var(--navy); color: #fff; }

  .tab {
    position: absolute;
    left: 102px;
    width: 143px;
    height: 29px;
    background: var(--navy);
  }
  .tab-top { top: 0; }
  .tab-bottom { bottom: 0; }

  .brand {
    position: absolute;
    top: 100px;
    left: 0;
    width: 100%;
    text-align: center;
    color: var(--navy);
    font-weight: 700;
  }
  .brand-mark {
    display: block;
    width: 44px;
    height: 44px;
    margin: 0 auto 38px;
    background: var(--navy);
  }
  .brand-name {
    display: block;
    font-size: 50px;
    line-height: 52px;
    letter-spacing: -0.5px;
  }
  .brand-sub {
    display: block;
    font-size: 23px;
    line-height: 28px;
    letter-spacing: 2px;
    margin-top: 2px;
  }

  .holder {
    position: absolute;
    top: 322px;
    left: 0;
    width: 100%;
    text-align: center;
  }
  .holder-name {
    font-size: 20px;
    font-weight: 700;
    color: var(--navy);
    line-height: 24px;
  }
  .holder-title {
    font-size: 15px;
    line-height: 20px;
    color: var(--text-grey);
  }

  .contacts {
    position: absolute;
    top: 385px;
    left: 0;
    width: 100%;
    list-style: none;
    text-align: center;
    font-size: 15.5px;
    line-height: 23.5px;
    color: var(--text-grey);
  }
  .contact-label {
    font-weight: 700;
    color: var(--navy);
    font-size: 14px;
    margin-right: 6px;
  }
  .contact-icon {
    width: 11px;
    height: 11px;
    vertical-align: -1px;
    margin-right: 6px;
  }

  .back-wordmark {
    position: absolute;
    top: 140px;
    left: 0;
    width: 100%;
    text-align: center;
    font-size: 54px;
    font-weight: 700;
    color: var(--navy-soft);
  }
  .addresses {
    position: absolute;
    top: 366px;
    left: 0;
    width: 100%;
    text-align: center;
  }
  .addresses-heading {
    font-size: 17.5px;
    font-weight: 600;
    line-height: 24px;
    margin-bottom: 14px;
  }
  .office {
    font-style: normal;
    font-size: 15.5px;
    line-height: 21px;
    margin-bottom: 15px;
  }
</style>
</head>
<body>

  <section class="card card-front" aria-label="Business card front">
    <div class="tab tab-top"></div>

    <div class="brand">
      <span class="brand-mark"></span>
      <span class="brand-name">BrivoPeak</span>
      <span class="brand-sub">PARTNERS</span>
    </div>

    <div class="holder">
      <p class="holder-name">Daniel Reyes</p>
      <p class="holder-title">Managing Director</p>
    </div>

    <ul class="contacts">
      <li><span class="contact-label">US :</span>(555) 214-7730</li>
      <li><span class="contact-label">UK :</span>+44 7700 900412</li>
      <li>
        <svg class="contact-icon" viewBox="0 0 12 12" aria-hidden="true">
          <rect x="0.5" y="2" width="11" height="8" fill="#132d54"/>
          <path d="M0.5 2.5 L6 6.5 L11.5 2.5" fill="none" stroke="#fff" stroke-width="1"/>
        </svg>info@brivopeakpartners.com
      </li>
      <li>
        <svg class="contact-icon" viewBox="0 0 12 12" aria-hidden="true">
          <circle cx="6" cy="6" r="5.5" fill="#132d54"/>
          <path d="M3 4 Q5 3 6 5 Q5 7 3.5 7 Z M7 7 Q9 6 9.5 8 Q8 9.5 7 9 Z" fill="#fff"/>
        </svg>www.brivopeakpartners.com
      </li>
    </ul>

    <div class="tab tab-bottom"></div>
  </section>

  <section class="card card-back" aria-label="Business card back">
    <div class="back-wordmark">BrivoPeak</div>

    <div class="addresses">
      <h2 class="addresses-heading">COMPANY ADDRESSES</h2>
      <address class="office">418 N Maple Ave, Suite 210-215<br>Fairview UT 84629 United States</address>
      <address class="office">14-16 Harbour Street London<br>EC2 4LP Great Britain</address>
    </div>
  </section>

</body>
</html>
```